Brisa Lumen Systems Corp Business Cards

Business cards to match the logo.

Company is a start up water technology company that has developed a patented system using centrifugal force to separate waste from municipal waste water to produce crystal clear clean water. Product sell starting at 2 million to governments both in the US and international.

Business cards should have a professional look with the target generally engineers.

Target Market(s)

Engineers, Government officials and investors

Industry/Entity Type

Water Treatment

Contact Information for Business Card

Business cards design will be used for 6 to 8 people with job titles. Can use the quote "If there is magic in the planet, it is contained in water." but not required to use quote. Should follow theme of Logo

Font styles to use
Other font styles liked:
• match logo font

Requirements
Nice to have
• Colors to match Logo. Business cards to match style of flow of Logo.
• Emphasis on clean look not a busy look. Clean flowing water.
Should not have
• Pictures of industrial equipment or wastewater

```html
<!DOCTYPE html>
<html lang="en">
<head>
<meta charset="utf-8">
<title>Brisa Lumen Systems Corp Business Cards</title>
<link rel="stylesheet" href="https://fonts.googleapis.com/css2?family=Cinzel:wght@600&family=Cormorant+Garamond:wght@500;600&family=Fondamento&display=swap">
<style>
  :root {
    --navy: #0f5387;
    --deep: #0a4d80;
    --sky: #2ea3dc;
    --bright: #35aee6;
    --paper: #ffffff;
    --stage: #2b2b2d;
  }
  * { margin: 0; padding: 0; box-sizing: border-box; }
  html, body { width: 1200px; height: 904px; overflow: hidden; background: var(--stage); }
  .sheet {
    width: 1200px; height: 904px;
    display: flex; flex-direction: column; align-items: center; justify-content: center; gap: 44px;
  }
  .card {
    position: relative; width: 640px; height: 366px; border-radius: 22px; overflow: hidden;
  }
  /* Back */
  .card--back {
    background: linear-gradient(160deg, var(--bright) 0%, #1f7fbd 50%, var(--deep) 100%);
    color: var(--paper);
  }
  .card--back .brand {
    position: absolute; top: 118px; left: 0; right: 0; text-align: center;
    font-family: "Cinzel", serif; font-weight: 600; font-size: 38px; letter-spacing: 2px; line-height: 1.1;
  }
  .card--back .brand span { display: block; font-size: 20px; letter-spacing: 9px; }
  .card--back .quote {
    position: absolute; bottom: 70px; left: 0; right: 0; text-align: center;
    font-family: "Fondamento", cursive; font-size: 19px;
  }
  /* Front */
  .card--front { background: linear-gradient(180deg, var(--paper) 60%, #eef1f3 100%); color: var(--navy); }
  .card--front .brand {
    position: absolute; top: 70px; left: 40px; width: 300px;
    font-family: "Cinzel", serif; font-weight: 600; font-size: 34px; line-height: 1.05; color: var(--navy);
  }
  .card--front .brand span { display: block; font-size: 17px; letter-spacing: 7px; }
  .rule { position: absolute; height: 1.5px; background: var(--navy); }
  .rule--brand { top: 160px; left: 40px; width: 250px; }
  .rule--bridge { top: 120px; left: 300px; width: 300px; opacity: .8; }
  .person {
    position: absolute; top: 66px; right: 40px; text-align: right;
    font-family: "Cinzel", serif; font-weight: 600;
  }
  .person .name { font-size: 25px; letter-spacing: 1px; }
  .person .title { font-size: 12px; letter-spacing: 4px; margin-top: 2px; }
  .address {
    position: absolute; top: 134px; right: 40px; text-align: right;
    font-family: "Cormorant Garamond", serif; font-weight: 600; font-size: 16px; line-height: 1.3;
  }
  .contact {
    position: absolute; top: 176px; left: 40px; list-style: none;
    font-family: "Cormorant Garamond", serif; font-weight: 600; font-size: 17px;
  }
  .contact li { display: flex; align-items: center; gap: 10px; height: 27px; }
  .contact svg { width: 18px; height: 18px; flex: none; }
  .waves { position: absolute; left: 0; bottom: 0; width: 640px; height: 110px; }
</style>
</head>
<body>
<main class="sheet">
  <section class="card card--back" aria-label="Card back">
    <h1 class="brand">Brisa Lumen<span>Systems Corp</span></h1>
    <p class="quote">If there is magic in the planet, it is contained in water.</p>
  </section>

  <section class="card card--front" aria-label="Card front">
    <h2 class="brand">Brisa Lumen<span>Systems Corp</span></h2>
    <div class="rule rule--bridge"></div>
    <div class="rule rule--brand"></div>

    <div class="person">
      <p class="name">Marten Holloway</p>
      <p class="title">Managing Director</p>
    </div>
    <p class="address">418 Harbor Crest Lane<br>Alder WA 98021</p>

    <ul class="contact">
      <li>
        <svg viewBox="0 0 20 20"><circle cx="10" cy="10" r="10" fill="var(--navy)"/><path d="M7 5.5l2 2-1 1.3c.6 1.4 1.7 2.5 3.1 3.1l1.3-1 2 2-1.2 1.4c-3.4-.3-7-3.9-7.3-7.3z" fill="#fff"/></svg>
        206-555-0142
      </li>
      <li>
        <svg viewBox="0 0 20 20"><circle cx="10" cy="10" r="10" fill="var(--navy)"/><rect x="5" y="6.5" width="10" height="7" fill="none" stroke="#fff" stroke-width="1.2"/><path d="M5 6.5l5 4 5-4" fill="none" stroke="#fff" stroke-width="1.2"/></svg>
        info@brisalumensystems.com
      </li>
      <li>
        <svg viewBox="0 0 20 20"><circle cx="10" cy="10" r="10" fill="var(--navy)"/><g fill="none" stroke="#fff" stroke-width="1.1"><circle cx="10" cy="10" r="5.5"/><ellipse cx="10" cy="10" rx="2.4" ry="5.5"/><path d="M4.5 10h11M5.5 7h9M5.5 13h9"/></g></svg>
        www.brisalumensystems.com
      </li>
    </ul>

    <svg class="waves" viewBox="0 0 640 110" preserveAspectRatio="none" aria-hidden="true">
      <path d="M0 70 C160 78 330 60 640 0 L640 110 L0 110 Z" fill="var(--bright)"/>
      <path d="M0 82 C170 88 350 70 640 14 L640 110 L0 110 Z" fill="var(--paper)"/>
      <path d="M0 92 C180 96 360 82 640 24 L640 110 L0 110 Z" fill="var(--deep)"/>
    </svg>
  </section>
</main>
</body>
</html>
```